App to track miniature golf scores and provides clues to puzzles (Pemberly Under Glass)

A mini-golf scorecard, selfies, badges, rules and clues. See attached for details. The coding and deployment will be provided by someone else, but those requirements are also listed in doc. We need to be able to update any text fields after design is handed over. This app is only for ios.

Target Market(s)

Families

Industry/Entity Type

Entertainment

Requirements
Must have
• The pages listed in the document is needed. Colors are also provided.
Nice to have
• Small animation effects
Should not have
• dark or psychedelic

```html
<!DOCTYPE html>
<html lang="en">
<head>
<meta charset="utf-8">
<title>Gameplay Rules – Pemberly Under Glass</title>
<link href="https://fonts.googleapis.com/css2?family=Fjalla+One&family=Barlow+Semi+Condensed:wght@400;500&display=swap" rel="stylesheet">
<style>
  :root {
    --bg: #ffffff;
    --ink: #1f1f24;
    --ink-soft: #3a3a42;
    --yellow: #fde39a;
    --pink: #f2a7c6;
    --pink-deep: #e07aa6;
    --violet: #d689ef;
    --purple: #8a1fae;
    --mint: #87efc2;
    --screen-edge: #d9d9de;
  }
  * { box-sizing: border-box; margin: 0; padding: 0; }
  html, body { width: 1200px; height: 675px; overflow: hidden; background: var(--bg); }
  .slide { position: relative; width: 1200px; height: 675px; overflow: hidden; background: var(--bg); }
  .deco { position: absolute; top: 0; left: 0; }

  .intro { position: absolute; left: 271px; top: 210px; width: 345px; color: var(--ink); }
  .intro-title { font-family: "Fjalla One", sans-serif; font-size: 25px; font-weight: 400; letter-spacing: 0.5px; margin-bottom: 18px; }
  .intro-text { font-family: "Barlow Semi Condensed", sans-serif; font-size: 14.5px; line-height: 17px; color: var(--ink-soft); }

  .screen {
    position: absolute; left: 787px; top: 80px; width: 232px; height: 512px;
    border-radius: 30px; border: 1px solid var(--screen-edge);
    background: var(--bg); overflow: hidden;
  }
  .screen-art { position: absolute; inset: 0; }
  .status-time { position: absolute; left: 22px; top: 10px; font-family: "Barlow Semi Condensed", sans-serif; font-size: 9px; font-weight: 500; color: var(--ink); }
  .app-bar { position: absolute; left: 14px; right: 14px; top: 34px; height: 22px; display: flex; align-items: center; }
  .back-arrow { width: 18px; height: 14px; }
  .app-title { flex: 1; text-align: center; font-family: "Fjalla One", sans-serif; font-size: 16px; color: var(--ink); margin-right: 18px; }

  .rule { position: absolute; left: 14px; width: 196px; color: var(--ink); }
  .rule-num { font-family: "Fjalla One", sans-serif; font-size: 18px; line-height: 20px; }
  .rule-text { font-family: "Barlow Semi Condensed", sans-serif; font-size: 9.5px; line-height: 11px; margin-top: 2px; }
  .rule-fade { color: #9a9aa2; }

  .next-button {
    position: absolute; left: 46px; top: 466px; width: 136px; height: 31px;
    border: 1.5px solid var(--ink); background: var(--bg);
    font-family: "Fjalla One", sans-serif; font-size: 11px; color: var(--ink);
    display: flex; align-items: center; justify-content: center; letter-spacing: 0.4px;
  }
</style>
</head>
<body>
<main class="slide">
  <svg class="deco" width="1200" height="675" viewBox="0 0 1200 675" aria-hidden="true">
    <polygon points="0,0 225,0 110,200 0,95" fill="var(--yellow)"/>
    <circle cx="1104" cy="52" r="73" fill="var(--pink)"/>
    <polygon points="1200,310 1200,470 1114,390" fill="var(--violet)"/>
    <circle cx="62" cy="656" r="96" fill="var(--mint)"/>
  </svg>

  <section class="intro">
    <h1 class="intro-title">RULES</h1>
    <p class="intro-text">After logging in. Users will see this screen where all the game rules are listed.<br>User can go on next screen or back to login screen.</p>
  </section>

  <section class="screen" aria-label="Gameplay rules screen">
    <svg class="screen-art" width="232" height="512" viewBox="0 0 232 512" aria-hidden="true">
      <circle cx="22" cy="30" r="60" fill="var(--pink)"/>
      <circle cx="215" cy="88" r="26" fill="var(--pink)"/>
      <polygon points="0,355 55,345 85,420 0,450" fill="var(--yellow)"/>
      <polygon points="232,375 232,512 150,512" fill="var(--mint)"/>
      <polygon points="130,68 135,73 130,78 125,73" fill="var(--purple)"/>
      <line x1="160" y1="120" x2="154" y2="132" stroke="var(--purple)" stroke-width="2"/>
      <rect x="205" y="195" width="6" height="6" fill="var(--pink-deep)"/>
      <line x1="68" y1="243" x2="60" y2="253" stroke="var(--mint)" stroke-width="2"/>
      <circle cx="185" cy="317" r="3" fill="var(--purple)"/>
      <line x1="88" y1="410" x2="82" y2="420" stroke="var(--pink-deep)" stroke-width="2"/>
    </svg>

    <span class="status-time">9:41</span>
    <header class="app-bar">
      <svg class="back-arrow" viewBox="0 0 18 14" aria-label="Back"><path d="M17 7H2M7 1.5L1.5 7 7 12.5" fill="none" stroke="var(--ink)" stroke-width="1.8"/></svg>
      <h2 class="app-title">GAMEPLAY RULES</h2>
    </header>

    <div class="rule" style="top:73px"><div class="rule-num">01.</div><p class="rule-text">Don't take pictures that reveal puzzle answers or clues.</p></div>
    <div class="rule" style="top:132px"><div class="rule-num">02.</div><p class="rule-text">Please carryout any specific instructions noted after a hole is completed.</p></div>
    <div class="rule" style="top:198px"><div class="rule-num">03.</div><p class="rule-text">Use props, buttons, knobs, levers or other puzzle elements with care. Don't use force or roughness.</p></div>
    <div class="rule" style="top:275px"><div class="rule-num">04.</div><p class="rule-text">Don't swing putter carelessly. Strokes should not be above knees.</p></div>
    <div class="rule" style="top:336px"><div class="rule-num">05.</div><p class="rule-text">Don't loft or hit the ball too hard!</p></div>
    <div class="rule" style="top:384px"><div class="rule-num">06.</div><p class="rule-text">Don't stand or climb on props.</p></div>
    <div class="rule" style="top:427px"><div class="rule-num">07.</div><p class="rule-text rule-fade">Do not stand on holes or playfield objects in any way.</p></div>

    <div class="next-button">NEXT</div>
  </section>
</main>
</body>
</html>
```